Add words, element to an already make product design

Hi guys,
I m already have the design (attached) which is a wet tissue product. The front main side (about 14cm x 7 cm) is the waves and the brand name Zelfo. However, in this main side, it should contain more words, which are "Khan uot" (mean wet wipe), and the words "Mat lanh" (mean cooling) and "Tinh khiet" (mean purity). "Khan uot" to indicate function of the product, while Mat lanh and Tinh khiet are just marketing term to add.
So yes, the task is quite simple, but I think the key is to choose an appropriate font, color and the location you decide where it should be. You can add any element you want, as long as it look good overall, and those words above, are required to have. More in the attached are few rival from our market, as some example.
Thank you, and wait your idea.

Hi guys, Just to tell you that the main front design will not change. So the waves and the brand name still keep the same. Just adding more words or elements to it. Thank you guys.

```html
<!DOCTYPE html>
<html lang="vi">
<head>
<meta charset="utf-8">
<title>Zelfo – khăn ướt, dieline bao bì</title>
<link rel="stylesheet" href="https://fonts.googleapis.com/css2?family=Kaushan+Script&family=Roboto:wght@400;500&display=swap">
<style>
  :root {
    --paper: #ffffff;
    --ink: #111111;
    --brand-blue: #3bbfef;
    --info-blue: #2a9be0;
    --sea-deep: #2f93e4;
    --sea-mid: #49c6ee;
    --sea-light: #bff2f6;
    --swatch: #3fc2ee;
  }
  html, body {
    margin: 0;
    width: 950px;
    height: 1200px;
    overflow: hidden;
    background: var(--paper);
  }
  .dieline { display: block; width: 950px; height: 1200px; }
  .fold { stroke: var(--ink); stroke-width: 3; stroke-dasharray: 30 14; fill: none; }
  .dimension { font-family: "Roboto", Arial, sans-serif; fill: var(--ink); }
  .dimension--large { font-size: 56px; }
  .dimension--small { font-size: 40px; }
  .info-text { font-family: "Roboto", Arial, sans-serif; font-size: 15px; fill: var(--info-blue); }
  .info-text--caps { font-size: 12px; }
  .icon-box { fill: none; stroke: var(--info-blue); stroke-width: 2.5; }
  .icon-mark { fill: none; stroke: var(--info-blue); stroke-width: 3; stroke-linecap: round; }
  .cert-badge { fill: var(--paper); stroke: var(--info-blue); stroke-width: 3; }
  .cert-band { fill: var(--info-blue); }
  .brand-name { font-family: "Kaushan Script", cursive; font-size: 230px; fill: var(--brand-blue); }
  .tagline { font-family: "Kaushan Script", cursive; font-size: 64px; fill: var(--paper); }
  .label-area { fill: var(--paper); }
  .swatch { fill: var(--swatch); }
  .swatch-label { font-family: "Roboto", Arial, sans-serif; font-size: 16px; fill: var(--ink); }
</style>
</head>
<body>
<svg class="dieline" viewBox="0 0 1700 2200" preserveAspectRatio="xMidYMid meet" xmlns="http://www.w3.org/2000/svg">
  <defs>
    <linearGradient id="sea" x1="0" y1="0" x2="0" y2="1">
      <stop offset="0" stop-color="#ffffff"/>
      <stop offset="0.12" stop-color="#e4f8fb"/>
      <stop offset="0.3" stop-color="var(--sea-light)"/>
      <stop offset="0.45" stop-color="var(--sea-mid)"/>
      <stop offset="0.55" stop-color="var(--sea-deep)"/>
      <stop offset="0.75" stop-color="#3fb4ef"/>
      <stop offset="1" stop-color="var(--sea-deep)"/>
    </linearGradient>
  </defs>

  <!-- sea artwork on front panel -->
  <path role="img" aria-label="Watercolour sea waves in light cyan to deep blue"
        fill="url(#sea)"
        d="M318 1095 C420 1160 520 1180 650 1170 C800 1160 900 1120 1050 1140 C1200 1155 1300 1190 1382 1170 L1382 1750 L318 1750 Z"/>

  <!-- fold and cut lines -->
  <g class="fold">
    <rect x="220" y="548" width="1260" height="1300"/>
    <line x1="318" y1="548" x2="318" y2="1848"/>
    <line x1="1382" y1="548" x2="1382" y2="1848"/>
    <line x1="220" y1="646" x2="1480" y2="646"/>
    <line x1="220" y1="922" x2="1480" y2="922"/>
    <line x1="220" y1="1474" x2="1480" y2="1474"/>
    <line x1="220" y1="1750" x2="1480" y2="1750"/>
  </g>

  <!-- dimensions -->
  <g class="dimension">
    <text class="dimension--small" x="280" y="527" text-anchor="middle">12.5</text>
    <text class="dimension--large" x="848" y="530" text-anchor="middle">135</text>
    <text class="dimension--small" x="1430" y="527" text-anchor="middle">12.5</text>
    <text class="dimension--large" x="845" y="1918" text-anchor="middle">160 mm</text>
    <text class="dimension--large" transform="translate(208 1200) rotate(-90)" text-anchor="middle">165mm</text>
    <text class="dimension--small" transform="translate(1508 580) rotate(90)" text-anchor="middle">12.5</text>
    <text class="dimension--small" transform="translate(1508 747) rotate(90)" text-anchor="middle">35</text>
    <text class="dimension--small" transform="translate(1508 1157) rotate(90)" text-anchor="middle">70</text>
    <text class="dimension--small" transform="translate(1508 1577) rotate(90)" text-anchor="middle">35</text>
    <text class="dimension--small" transform="translate(1508 1802) rotate(90)" text-anchor="middle">12.5</text>
  </g>

  <!-- top panel info -->
  <text class="info-text" x="672" y="730">NSX: 2 năm trước HSD</text>
  <text class="info-text" x="672" y="747">HSD: In trên bao bì</text>

  <g class="info-text info-text--caps" transform="rotate(180 466 778)">
    <text x="466" y="774" text-anchor="middle">XIN BỎ VÀO ĐÚNG</text>
    <text x="466" y="790" text-anchor="middle">NƠI QUY ĐỊNH</text>
  </g>

  <g class="usage-icons">
    <rect class="icon-box" x="445" y="803" width="42" height="42" rx="6"/>
    <path class="icon-mark" d="M456 835 L476 813"/>
    <rect class="icon-box" x="530" y="757" width="42" height="42" rx="6"/>
    <path class="icon-mark" d="M540 788 L562 766"/>
    <rect class="icon-box" x="586" y="757" width="42" height="42" rx="6"/>
    <circle class="icon-mark" cx="604" cy="778" r="9"/>
    <rect class="icon-box" x="642" y="757" width="42" height="42" rx="6"/>
    <path class="icon-mark" d="M650 790 L676 766 M656 770 L672 786"/>
    <rect class="icon-box" x="530" y="811" width="42" height="42" rx="6"/>
    <path class="icon-mark" d="M538 823 H564 M542 836 H560"/>
    <rect class="icon-box" x="586" y="811" width="42" height="42" rx="6"/>
    <circle class="icon-mark" cx="607" cy="832" r="10"/>
    <rect class="icon-box" x="642" y="811" width="42" height="42" rx="6"/>
    <path class="icon-mark" d="M650 832 H676"/>
  </g>

  <g class="certificate" aria-label="Certificate badge">
    <path class="cert-badge" d="M1172 765 Q1238 705 1304 765 L1304 840 Q1238 870 1172 840 Z"/>
    <rect class="cert-band" x="1165" y="752" width="146" height="20"/>
  </g>

  <!-- front panel -->
  <text class="brand-name" x="850" y="1275" text-anchor="middle">Zelfo</text>

  <text class="tagline" x="470" y="1440" text-anchor="middle">mat lanh</text>
  <text class="tagline" x="850" y="1440" text-anchor="middle">tinh khiet</text>
  <text class="tagline" x="1210" y="1440" text-anchor="middle">khan uot</text>

  <rect class="label-area" x="1035" y="1527" width="300" height="116"/>

  <!-- colour swatch -->
  <rect class="swatch" x="220" y="1770" width="39" height="77"/>
  <text class="swatch-label" transform="translate(225 1775) rotate(90)">BH</text>
</svg>
</body>
</html>
```